Redesign Business Cards, Attached

Please read instructions carefully. If you have any questions send a message before submitting your ONE design. Please redesign attached business cards. Double sided. Use same content and descriptions. Use black, silver, crimson red and gold colors. My only issue with the attached design is the background colors. I like the layout as-is. I can provide the individual pictures on the back side later. Do not submit more than one design. One submission shall include both front and back. Do not submit front and back separately. A second project will be launched to create a matching post card after completion of this.
Industry/Entity Type
see description and attachments.
Contact Information for Business Card
Requirements
Must have
- see description and attachments.
Nice to have
Should not have

```html
<!DOCTYPE html>
<html lang="en">
<head>
<meta charset="utf-8">
<title>Harborline Boat Training – Business Card</title>
<link rel="stylesheet" href="https://fonts.googleapis.com/css2?family=Poppins:wght@400;500;600;700&family=Fira+Sans+Condensed:ital,wght@1,400;1,500&display=swap">
<style>
  :root {
    --backdrop: #7e7e7e;
    --ink: #111214;
    --night: #1c2126;
    --crimson: #dc1a40;
    --gold: #bf9a1c;
    --silver: #e4e4e4;
    --paper: #f5f5f5;
    --white: #ffffff;
    --sea-deep: #2b4a66;
    --sea-light: #8fb0c9;
  }
  * { box-sizing: border-box; margin: 0; padding: 0; }
  html, body { width: 1093px; height: 1200px; overflow: hidden; }
  body {
    background: var(--backdrop);
    font-family: "Poppins", sans-serif;
    position: relative;
  }
  .card {
    position: absolute;
    left: 256px;
    width: 580px;
    height: 357px;
    overflow: hidden;
    background: var(--night);
  }
  .card--front { top: 226px; }
  .card--back { top: 620px; }
  .card-shapes { position: absolute; inset: 0; width: 100%; height: 100%; }

  /* Front */
  .brand-mark {
    position: absolute;
    left: 38px; top: 104px;
    width: 150px; height: 150px;
    border-radius: 50%;
    background: var(--white);
    border: 6px solid var(--gold);
    display: flex; align-items: center; justify-content: center;
    text-align: center;
  }
  .brand-name {
    font-weight: 600;
    font-size: 17px;
    line-height: 1.2;
    color: var(--ink);
  }
  .holder-name {
    position: absolute;
    left: 323px; top: 82px;
    font-weight: 600;
    font-size: 23px;
    letter-spacing: 0.2px;
    color: var(--crimson);
  }
  .holder-title {
    position: absolute;
    left: 323px; top: 107px;
    font-size: 18px;
    line-height: 21px;
    color: var(--ink);
  }
  .text-pill {
    position: absolute;
    left: 319px; top: 175px;
    width: 223px; height: 39px;
    border-radius: 20px;
    background: var(--crimson);
    color: var(--white);
    font-weight: 600;
    font-size: 17px;
    display: flex; align-items: center; justify-content: center; gap: 6px;
  }
  .text-pill svg { width: 16px; height: 16px; }
  .contact-line {
    position: absolute;
    left: 321px;
    display: flex; align-items: center; gap: 8px;
    font-size: 15.5px;
    color: var(--ink);
  }
  .contact-line svg { width: 15px; height: 15px; flex: none; }
  .contact-line--email { top: 236px; }
  .contact-line--web { top: 258px; }

  /* Back */
  .instructor-label {
    position: absolute;
    left: 52px; top: 124px;
    font-weight: 600;
    font-size: 9.5px;
    letter-spacing: 0.3px;
    color: var(--silver);
  }
  .service-tile {
    position: absolute;
    width: 137px; height: 66px;
    clip-path: polygon(22px 0, 100% 0, calc(100% - 22px) 100%, 0 100%);
    display: flex; align-items: center; justify-content: center;
    text-align: center;
    font-family: "Fira Sans Condensed", sans-serif;
    font-style: italic;
    font-size: 14.5px;
    line-height: 15px;
    color: var(--white);
  }
  .service-tile--black { background: var(--ink); }
  .service-tile--red { background: var(--crimson); }
  .row-one { top: 164px; }
  .row-two { top: 242px; }
  .site-line {
    position: absolute;
    left: 0; right: 0; top: 320px;
    text-align: center;
    font-weight: 600;
    font-size: 18px;
    color: var(--ink);
  }
</style>
</head>
<body>

<section class="card card--front" aria-label="Business card front">
  <svg class="card-shapes" viewBox="0 0 972 600" preserveAspectRatio="none">
    <defs>
      <linearGradient id="nightWater" x1="0" y1="0" x2="1" y2="1">
        <stop offset="0" stop-color="#2a3036"/>
        <stop offset="1" stop-color="#15191d"/>
      </linearGradient>
    </defs>
    <rect width="972" height="600" fill="url(#nightWater)" role="img" aria-label="Dark photo of a motor boat cruising on open water"/>
    <polygon points="403,58 441,0 546,0 461,148" fill="var(--gold)"/>
    <polygon points="403,556 441,600 546,600 461,459" fill="var(--gold)"/>
    <polygon points="546,0 972,0 972,600 546,600 382,300" fill="var(--white)"/>
    <polygon points="562,0 972,0 972,600 562,600 398,300" fill="var(--silver)"/>
  </svg>

  <div class="brand-mark"><span class="brand-name">Harborline<br>Boat Training</span></div>

  <h1 class="holder-name">DALTON R. HAVERLY</h1>
  <p class="holder-title">USCG Licensed Captain<br>Certified Instructor</p>

  <div class="text-pill">
    <span>TEXT</span>
    <svg viewBox="0 0 24 24" aria-hidden="true"><path fill="none" stroke="currentColor" stroke-width="2" d="M5 3h4l2 5-2.5 1.5a11 11 0 0 0 6 6L16 13l5 2v4a2 2 0 0 1-2 2A16 16 0 0 1 3 5a2 2 0 0 1 2-2z"/></svg>
    <span>(555) 014-2290</span>
  </div>

  <p class="contact-line contact-line--email">
    <svg viewBox="0 0 24 24" aria-hidden="true"><rect x="1" y="4" width="22" height="16" fill="var(--crimson)"/><path d="M1 5l11 8 11-8" fill="none" stroke="var(--white)" stroke-width="1.8"/></svg>
    service@helmready.com
  </p>
  <p class="contact-line contact-line--web">
    <svg viewBox="0 0 24 24" aria-hidden="true"><g fill="none" stroke="var(--crimson)" stroke-width="2"><circle cx="12" cy="12" r="10"/><ellipse cx="12" cy="12" rx="4.5" ry="10"/><path d="M2 12h20M4 7h16M4 17h16"/></g></svg>
    www.HelmReady.com
  </p>
</section>

<section class="card card--back" aria-label="Business card back">
  <svg class="card-shapes" viewBox="0 0 972 600" preserveAspectRatio="none">
    <defs>
      <linearGradient id="dayWater" x1="0" y1="0" x2="1" y2="1">
        <stop offset="0" stop-color="var(--sea-deep)"/>
        <stop offset="1" stop-color="var(--sea-light)"/>
      </linearGradient>
    </defs>
    <rect width="972" height="600" fill="var(--paper)"/>
    <rect width="972" height="330" fill="url(#nightWater)" role="img" aria-label="Dark photo of open water"/>
    <polygon points="492,36 516,0 568,0 514,73" fill="var(--gold)"/>
    <polygon points="574,0 972,0 972,330 528,330 468,161" fill="var(--white)"/>
    <polygon points="582,0 972,0 972,330 540,330 480,161" fill="url(#dayWater)" role="img" aria-label="Photo of a white center-console boat speeding across sunlit water"/>
    <circle cx="136" cy="140" r="58" fill="var(--silver)"/>
    <circle cx="294" cy="146" r="58" fill="var(--silver)"/>
  </svg>

  <span class="instructor-label">INSTRUCTOR</span>

  <div class="service-tile service-tile--black row-one" style="left:51px">Hands-On<br>Boat<br>Training</div>
  <div class="service-tile service-tile--red row-one" style="left:177px">Introduction<br>to Power<br>boating</div>
  <div class="service-tile service-tile--black row-one" style="left:303px">Precision<br>Docking &amp;<br>Boat Handling</div>
  <div class="service-tile service-tile--red row-one" style="left:427px">Open Water<br>Boat<br>Handling</div>

  <div class="service-tile service-tile--red row-two" style="left:27px">Island<br>Anchoring</div>
  <div class="service-tile service-tile--black row-two" style="left:153px">Open Water<br>Advanced<br>Maneuvers</div>
  <div class="service-tile service-tile--red row-two" style="left:278px">Coastal<br>Navigation</div>
  <div class="service-tile service-tile--black row-two" style="left:402px">Captaining/<br>Piloting Service<br>for Your Outings</div>

  <p class="site-line">www.HelmReady.com</p>
</section>

</body>
</html>
```